Healthcare marketing Website design

This is for a healthcare marketing agency
All details and brief included in the files

I need the design to be incredible!

5 pages to be designed
Home page
About
Portfolio Page
Services
Start your project page

If you need more stock images - download preview images from kelmora pix so I can purchase at a later date

```html
<!DOCTYPE html>
<html lang="en">
<head>
<meta charset="utf-8">
<title>Keystep Consulting – Healthcare Marketing</title>
<link href="https://fonts.googleapis.com/css2?family=Comfortaa:wght@400;600;700&family=Arimo:wght@400;700&display=swap" rel="stylesheet">
<style>
:root{
  --navy:#1f3463;
  --navy-deep:#22386a;
  --blue:#1c8fd8;
  --ink:#1b2233;
  --text:#3a3f4a;
  --muted:#7a808c;
  --line:#dfe3ea;
  --footer:#0b0f1c;
  --star:#f5a623;
  --white:#fff;
}
*{box-sizing:border-box;margin:0;padding:0}
html,body{width:1200px;height:4518px;overflow:hidden}
body{position:relative;background:var(--white);font-family:"Arimo",Arial,sans-serif;color:var(--text)}
.abs{position:absolute}
.display{font-family:"Comfortaa","Trebuchet MS",sans-serif}
.btn{position:absolute;height:49px;border-radius:25px;font-family:"Comfortaa",sans-serif;font-weight:700;font-size:16px;display:flex;align-items:center;justify-content:center;text-decoration:none}
.btn-navy{background:var(--navy);color:#fff}
.btn-blue{background:var(--blue);color:#fff}
.btn-ghost{border:1.5px solid #fff;color:#fff}
.btn-white{background:#fff;color:var(--blue)}

/* hero */
.hero-bg{left:0;top:0;width:1200px;height:700px;background:linear-gradient(100deg,#f4f7fa 0%,#e9eef4 45%,#c9d6e4 100%)}
.hero-visual{left:620px;top:60px;width:580px;height:620px;background:radial-gradient(circle at 55% 45%,#dce8f3 0%,#9eb6cf 55%,#6f86a3 100%);opacity:.9}
.topbar{left:509px;top:0;width:691px;height:40px;background:var(--blue);clip-path:polygon(4% 0,100% 0,100% 100%,0 100%);color:#fff;font-size:14px}
.topbar span{position:absolute;top:11px}
.soc{position:absolute;width:26px;height:26px;border:1.5px solid #fff;border-radius:50%}
.logo{left:110px;top:36px;display:flex;align-items:center;gap:10px;font-family:"Comfortaa",sans-serif;font-weight:700;font-size:34px;color:var(--blue)}
.logo i{width:30px;height:30px;border-radius:50%;background:var(--blue);display:block}
.nav{left:453px;top:74px;display:flex;gap:24px;font-size:13.5px;color:var(--ink)}
.nav .active{border-bottom:2px solid var(--ink);padding-bottom:3px}
.hero-title{left:110px;top:178px;width:480px;font-size:22px;line-height:43px;font-weight:600;color:var(--ink)}
.hero-sub{left:110px;top:268px;font-size:18px;font-weight:600;color:var(--ink)}
.hero-sub b{color:var(--blue);font-weight:600}
.bullets{left:110px;top:326px;width:480px;list-style:none;font-size:14.5px;line-height:22px;color:#2a3040}
.bullets li{padding-left:28px;position:relative;margin-bottom:13px}
.bullets li:before{content:"";position:absolute;left:2px;top:5px;width:11px;height:11px;background:var(--blue);transform:rotate(45deg)}
.hero-curve{left:0;top:640px}
.scroll-hint{left:588px;top:748px}

/* about */
.about-visual{left:110px;top:865px;width:399px;height:391px;border-radius:40px;background:linear-gradient(135deg,#3a4f86 0%,#7fa8d6 50%,#2b4277 100%)}
.about-kicker{left:598px;top:863px;font-size:23px;color:var(--blue);font-weight:700}
.about-title{left:598px;top:905px;font-size:30px;font-weight:400;color:var(--ink)}
.about-copy{left:598px;top:958px;width:492px;font-size:12.6px;line-height:25.8px;color:#333}

/* since */
.since-band{left:0;top:1349px;width:1200px;height:686px;background:linear-gradient(180deg,#263e74,var(--navy-deep))}
.since-mark{left:580px;top:1432px;width:40px;height:40px;border:3px solid #fff;border-radius:50%}
.since-title{left:0;top:1524px;width:1200px;text-align:center;font-size:32px;font-weight:400;color:#fff}
.since-copy{left:170px;top:1585px;width:860px;text-align:center;font-size:13.4px;line-height:25.6px;color:#fff}
.stat{position:absolute;top:1708px;width:220px;text-align:center;color:#fff;font-family:"Comfortaa",sans-serif;font-weight:700;font-size:16px;line-height:24px}
.stat .ic{width:88px;height:88px;margin:0 auto 14px;border-radius:50%;background:var(--blue);border:5px solid #3a7fc8;display:flex;align-items:center;justify-content:center}

/* section heads */
.sec-head{left:0;width:1200px;display:flex;justify-content:center;align-items:center;gap:14px;font-size:32px;font-weight:400;color:var(--ink)}
.sec-head i{width:20px;height:20px;background:var(--blue);display:block}

/* testimonials */
.card{position:absolute;width:302px;height:286px;background:#fff;border:1px solid var(--line);padding:38px 28px}
.card.raised{box-shadow:0 6px 22px rgba(20,30,60,.18);border-color:transparent}
.stars{color:var(--star);font-size:14px;letter-spacing:2px}
.card p{margin-top:18px;font-size:14px;line-height:26px;color:#333}
.who{display:flex;align-items:center;gap:18px;margin-top:18px}
.avatar{width:48px;height:48px;border-radius:50%;background:linear-gradient(#c8d2de,#8796a8)}
.who b{display:block;font-family:"Comfortaa",sans-serif;font-weight:600;font-size:17px;color:var(--blue)}
.who small{font-size:13.5px;color:var(--muted)}
.arrow{position:absolute;width:30px;height:30px;display:flex;align-items:center;justify-content:center}
.stetho{left:1000px;top:2526px;width:200px;height:170px;border-radius:50% 0 0 50%;background:radial-gradient(circle at 60% 50%,#f5b9c6,#d9dde3 70%,#fff 100%)}

/* faq */
.faq-bg{left:0;top:2701px;width:1200px;height:637px;background:linear-gradient(90deg,#f4f5f7,#e6e9ee)}
.qa{position:absolute;left:189px;width:821px;background:#fff;border:1px solid var(--line);padding:0 32px 0 18px}
.qa .q{height:66px;display:flex;align-items:center;gap:20px;font-family:"Comfortaa",sans-serif;font-weight:700;font-size:17px;color:var(--ink)}
.qa .q span:first-child{font-size:20px;font-weight:400}
.qa .q svg{margin-left:auto}
.qa .a{padding:0 40px 20px 70px;font-size:13px;line-height:24px;color:#333;margin-top:-6px}

/* blog */
.post{position:absolute;top:3503px;width:303px}
.post .ph{height:217px;border-radius:18px}
.post .date{margin-top:26px;font-family:"Comfortaa",sans-serif;font-weight:700;font-size:15px;color:var(--blue);display:flex;gap:10px;align-items:center}
.post h3{margin-top:20px;font-family:"Comfortaa",sans-serif;font-weight:400;font-size:24px;line-height:37px;color:var(--ink)}
.post p{margin-top:10px;font-size:13.5px;line-height:26px;color:#333}
.post a{display:flex;align-items:center;gap:12px;margin-top:16px;font-family:"Comfortaa",sans-serif;font-weight:700;font-size:16px;color:var(--blue);text-decoration:none}

/* footer */
.footer{left:0;top:4040px;width:1200px;height:478px}
.f-col{position:absolute;top:4155px;color:#fff}
.f-col h4{font-family:"Comfortaa",sans-serif;font-weight:400;font-size:21px;margin-bottom:24px}
.f-col ul{list-style:none;font-size:14.5px;line-height:26px}
.f-input{width:232px;height:42px;border:1px solid #9aa3b5;border-radius:21px;padding-left:20px;font-size:12px;color:#b8bfcc;display:flex;align-items:center;margin-bottom:18px}
.f-logo{left:110px;top:4212px;display:flex;align-items:center;gap:12px;font-family:"Comfortaa",sans-serif;font-weight:700;font-size:36px;color:#fff}
.f-logo i{width:34px;height:34px;border-radius:50%;background:#fff;display:block}
.f-soc{position:absolute;top:4313px;width:42px;height:42px;border-radius:50%;background:var(--blue)}
.copy{left:0;top:4463px;width:1200px;text-align:center;color:#fff;font-size:14px}
</style>
</head>
<body>

<!-- Hero -->
<div class="hero-bg abs"></div>
<div class="hero-visual abs" role="img" aria-label="Healthcare technology scene: hand holding a tablet with a glowing human body diagram and medical icons"></div>
<div class="topbar abs">
  <span style="left:60px">✉&nbsp; hello@keystepconsulting.example</span>
  <span style="left:340px">☎&nbsp; +1 (555) 014 2290</span>
  <i class="soc" style="left:507px;top:7px"></i>
  <i class="soc" style="left:543px;top:7px"></i>
</div>
<div class="logo abs"><i></i>keystep</div>
<nav class="nav abs">
  <span class="active">Home</span><span>About</span><span>Portfolio</span><span>Contact Us</span><span>Our Services</span><span>Blog</span>
</nav>
<a class="btn btn-blue" style="left:920px;top:60px;width:168px">Start your project</a>

<h1 class="hero-title abs display">Don’t miss a new opportunity to grow you practice with your online presence.</h1>
<div class="hero-sub abs display"><b>Being online:</b> a large opportunity for your practice</div>
<ul class="bullets abs">
  <li>80% of internet uses search for health information</li>
  <li>50% would like information about a specific health professional</li>
  <li>42% of individuals look at health related consumer reviews</li>
  <li>41% of consumers say online presence may impact their choice of health professional</li>
</ul>
<a class="btn btn-navy" style="left:110px;top:513px;width:120px">Contact Us</a>
<a class="btn btn-blue" style="left:251px;top:513px;width:167px">Start your project</a>

<svg class="hero-curve abs" width="1200" height="70" viewBox="0 0 1200 70">
  <path d="M0 0 C300 70 900 70 1200 0 L1200 70 L0 70Z" fill="#fff"/>
  <path d="M0 45 C300 40 600 52 1200 0 L1200 16 C600 70 300 60 0 62Z" fill="var(--blue)"/>
</svg>
<svg class="scroll-hint abs" width="24" height="34" viewBox="0 0 24 34">
  <rect x="2" y="2" width="20" height="30" rx="10" fill="none" stroke="var(--blue)" stroke-width="2"/>
  <path d="M12 9v12M8 17l4 4 4-4" fill="none" stroke="var(--blue)" stroke-width="2"/>
</svg>

<!-- About -->
<div class="about-visual abs" role="img" aria-label="Collage of healthcare photos: stethoscope, piggy bank, medical icons and a doctor with a laptop"></div>
<div class="about-kicker abs display">Keystep Consulting:</div>
<h2 class="about-title abs display">Helping Those Who Help Others.</h2>
<p class="about-copy abs">You became a health professional because you wanted to make a difference and you obviously care about patient outcomes. At first things were great and you had plenty of patients but in the last few years there’s more competition offering the same types of services and products that you do. Regular customers haven’t come back to you in a while and you know you NEED to do something but the old ways like relying on word of mouth doesn’t seem to be working well anymore and you don’t know how to get started. But that’s where we can help... Keystep Consulting specialises in helping health professionals like you to create a great online user experience for your patients.</p>
<a class="btn btn-navy" style="left:598px;top:1213px;width:126px">Contact Us</a>
<a class="btn btn-blue" style="left:738px;top:1213px;width:168px">Start your project</a>

<!-- Since 2015 -->
<div class="since-band abs"></div>
<div class="since-mark abs"></div>
<h2 class="since-title abs display">Helping Clients Since 2015</h2>
<p class="since-copy abs">Keystep consulting specialises in helping health professionals like you, stand out from the busy crowd, find new patient and helps you be seen as the go-to person within your industry. Unlike most health professionals who solely rely on word of mouth, we use the latest online marketing techniques to grow you and your practice.While our niche has always been in the healthcare industry, On Keystep Marketing also has experience in providing solutions our e-commerce partners as well as other professional industries.</p>
<div class="stat" style="left:314px"><div class="ic"><svg width="40" height="40" viewBox="0 0 40 40" fill="none" stroke="#fff" stroke-width="2"><path d="M20 10v20M10 20h20"/><circle cx="20" cy="20" r="15"/></svg></div>63% Healthcare<br>and medical</div>
<div class="stat" style="left:488px"><div class="ic"><svg width="40" height="40" viewBox="0 0 40 40" fill="none" stroke="#fff" stroke-width="2"><rect x="6" y="8" width="28" height="18" rx="2"/><path d="M14 32h12M20 26v6"/></svg></div>25% ecommerce<br>projects</div>
<div class="stat" style="left:664px"><div class="ic"><svg width="40" height="40" viewBox="0 0 40 40" fill="none" stroke="#fff" stroke-width="2"><circle cx="20" cy="20" r="6"/><circle cx="20" cy="20" r="14" stroke-dasharray="5 4"/></svg></div>12% other<br>professional services</div>
<a class="btn btn-ghost" style="left:447px;top:1902px;width:124px">Contact Us</a>
<a class="btn btn-white" style="left:586px;top:1902px;width:168px">Start your project</a>

<!-- Testimonials -->
<h2 class="sec-head abs display" style="top:2114px"><i></i>See what our clients say</h2>
<div class="arrow" style="left:62px;top:2325px;background:#9aa0aa"><svg width="10" height="12"><path d="M7 1L2 6l5 5" stroke="#fff" stroke-width="2" fill="none"/></svg></div>
<div class="arrow" style="left:1109px;top:2325px;background:var(--blue)"><svg width="10" height="12"><path d="M3 1l5 5-5 5" stroke="#fff" stroke-width="2" fill="none"/></svg></div>
<div class="card" style="left:110px;top:2198px"><div class="stars">★★★★★</div><p>Lorem ipsum dolor sit &nbsp;consectetur adipiscing elit, sed do eiusm tempor incididunt ut labore et dolore magna aliqua. Ut consequat.</p><div class="who"><div class="avatar"></div><div><b>Dalen Morrow</b><small>Lorem ipsum</small></div></div></div>
<div class="card raised" style="left:449px;top:2231px"><div class="stars">★★★★★</div><p>Lorem ipsum dolor sit &nbsp;consectetur adipiscing elit, sed do eiusm tempor incididunt ut labore et dolore magna aliqua. Ut consequat.</p><div class="who"><div class="avatar"></div><div><b>Dalen Morrow</b><small>Lorem ipsum</small></div></div></div>
<div class="card" style="left:786px;top:2198px"><div class="stars">★★★★★</div><p>Lorem ipsum dolor sit &nbsp;consectetur adipiscing elit, sed do eiusm tempor incididunt ut labore et dolore magna aliqua. Ut consequat.</p><div class="who"><div class="avatar"></div><div><b>Dalen Morrow</b><small>Lorem ipsum</small></div></div></div>
<a class="btn btn-navy" style="left:447px;top:2567px;width:124px">Contact Us</a>
<a class="btn btn-blue" style="left:586px;top:2567px;width:168px">Start your project</a>
<div class="stetho abs" role="img" aria-label="Stethoscope wrapped around a pink piggy bank"></div>

<!-- FAQ -->
<div class="faq-bg abs" role="img" aria-label="Soft grey background of a person working on a laptop"></div>
<h2 class="sec-head abs display" style="top:2770px"><i></i>Frequently Asked Questions</h2>
<div class="qa" style="top:2856px"><div class="q"><span>Q1</span><span>Lorem ipsum dolor sit amet, consectetur adipiscing elit, sed do</span><svg width="12" height="14"><path d="M3 2l5 5-5 5" stroke="#222" stroke-width="2" fill="none"/></svg></div></div>
<div class="qa" style="top:2940px"><div class="q"><span>Q2</span><span>Lorem ipsum dolor sit amet, consectetur adipiscing elit, sed do</span><svg width="14" height="12"><path d="M2 3l5 5 5-5" stroke="#222" stroke-width="2" fill="none"/></svg></div><div class="a">Lorem ipsum dolor sit amet, consectetur adipiscing elit, sed do eiusmod tempor incididunt ut labore et dolore magna aliqua.Ut enim ad minim veniam, quis nostrud exercitation ullamco laboris nisi ut aliquip ex ea commodo consequat.</div></div>
<div class="qa" style="top:3110px"><div class="q"><span>Q3</span><span>Lorem ipsum dolor sit amet, consectetur adipiscing elit, sed do</span><svg width="12" height="14"><path d="M3 2l5 5-5 5" stroke="#222" stroke-width="2" fill="none"/></svg></div></div>
<div class="qa" style="top:3194px"><div class="q"><span>Q4</span><span>Lorem ipsum dolor sit amet, consectetur adipiscing elit, sed do</span><svg width="12" height="14"><path d="M3 2l5 5-5 5" stroke="#222" stroke-width="2" fill="none"/></svg></div></div>

<!-- Blog -->
<h2 class="sec-head abs display" style="top:3422px"><i></i>Blog Post</h2>
<article class="post" style="left:110px"><div class="ph" role="img" aria-label="Hands typing on a laptop keyboard" style="background:linear-gradient(135deg,#e8eaee,#9da5b2)"></div><div class="date"><svg width="14" height="14"><rect x="1" y="2" width="12" height="11" fill="none" stroke="var(--blue)" stroke-width="2"/></svg>08 07 2022</div><h3>Lorem ipsum dolor sit amet, consectetur</h3><p>Lorem ipsum dolor sit amet, consectetur adipiscing elit, sed do eiusmod tempor</p><a>Learn More <svg width="28" height="14"><circle cx="7" cy="7" r="7" fill="var(--navy)"/><path d="M18 3l4 4-4 4" stroke="var(--blue)" stroke-width="2" fill="none"/></svg></a></article>
<article class="post" style="left:449px"><div class="ph" role="img" aria-label="Designers sketching website wireframes on paper" style="background:linear-gradient(135deg,#2d4a80,#7f9bbf)"></div><div class="date"><svg width="14" height="14"><rect x="1" y="2" width="12" height="11" fill="none" stroke="var(--blue)" stroke-width="2"/></svg>08 07 2022</div><h3>Lorem ipsum dolor sit amet, consectetur</h3><p>Lorem ipsum dolor sit amet, consectetur adipiscing elit, sed do eiusmod tempor</p><a>Learn More <svg width="28" height="14"><circle cx="7" cy="7" r="7" fill="var(--navy)"/><path d="M18 3l4 4-4 4" stroke="var(--blue)" stroke-width="2" fill="none"/></svg></a></article>
<article class="post" style="left:786px"><div class="ph" role="img" aria-label="Hand holding a smartphone with social media icons" style="background:linear-gradient(135deg,#c9ced6,#5d6878)"></div><div class="date"><svg width="14" height="14"><rect x="1" y="2" width="12" height="11" fill="none" stroke="var(--blue)" stroke-width="2"/></svg>08 07 2022</div><h3>Lorem ipsum dolor sit amet, consectetur</h3><p>Lorem ipsum dolor sit amet, consectetur adipiscing elit, sed do eiusmod tempor</p><a>Learn More <svg width="28" height="14"><circle cx="7" cy="7" r="7" fill="var(--navy)"/><path d="M18 3l4 4-4 4" stroke="var(--blue)" stroke-width="2" fill="none"/></svg></a></article>

<!-- Footer -->
<svg class="footer abs" width="1200" height="478" viewBox="0 0 1200 478">
  <path d="M0 35 L600 10 L1200 35 L1200 478 L0 478Z" fill="var(--footer)"/>
  <path d="M0 48 L600 0 L1200 48 L1200 40 L600 10 L0 40Z" fill="var(--blue)"/>
</svg>
<div class="f-logo abs"><i></i>keystep</div>
<i class="f-soc" style="left:112px"></i>
<i class="f-soc" style="left:165px"></i>
<div class="f-col" style="left:442px"><h4>Quick Links</h4><ul><li>Home</li><li>About</li><li>Portfolio</li><li>Contact Us</li><li>Our Services</li><li>Blog</li></ul></div>
<div class="f-col" style="left:638px"><h4>Other Links</h4><ul><li>Terms &amp; Conditions</li><li>Privacy Policy</li><li>About Us</li><li>Support</li></ul></div>
<div class="f-col" style="left:856px"><h4>Sign up to our mailing list</h4><div class="f-input">Full Name</div><div class="f-input">Email Address</div></div>
<a class="btn btn-blue" style="left:856px;top:4341px;width:110px;height:46px;font-size:14px">SEND</a>
<div class="copy abs">©Copyrights 2022 Keystep Consulting &nbsp;| &nbsp; All Rights Reserved</div>

</body>
</html>
```